Summer Drinks Flyer for Coffee Shop

We are a coffee shop in London and would like to have a cool and nice flyer for our summer drinks (juices and frozen drink) flyer - see on the attached file for the list

Attached you can find an "attempt" - please note that I would no necessary need the image below.

I also attache our new logo.

thank you

Industry/Entity Type

Coffee Shop

```html
<!DOCTYPE html>
<html lang="en">
<head>
<meta charset="utf-8">
<title>solavita — New Summer Drinks Menu</title>
<link rel="stylesheet" href="https://fonts.googleapis.com/css2?family=Roboto+Condensed:wght@400&family=Marck+Script&display=swap">
<style>
  :root {
    --backdrop: #efe6d6;
    --paper: #ffffff;
    --navy: #0c0c4a;
    --gold: #c0952f;
    --gold-edge: #b8912e;
    --ink: #14145a;
    --frame-pink: #ee22d4;
    --frame-yellow: #f3e600;
    --frame-blue: #1a1ae0;
  }
  * { margin: 0; padding: 0; box-sizing: border-box; }
  html, body { width: 862px; height: 1200px; overflow: hidden; }
  body { background: var(--backdrop); position: relative; font-family: "Roboto Condensed", "Arial Narrow", sans-serif; color: var(--ink); }

  .flyer { position: absolute; left: 40px; top: 108px; width: 750px; height: 1032px; background: var(--paper); box-shadow: 2px 3px 8px rgba(0,0,0,.25); }
  .flyer__edge { position: absolute; right: 0; top: 0; width: 11px; height: 100%; background: var(--gold-edge); }
  .flyer__header { position: absolute; left: 0; top: 44px; width: 739px; height: 258px; background: var(--navy); }
  .flyer__footer { position: absolute; left: 0; bottom: 0; width: 739px; height: 22px; background: var(--navy); }

  .brand { position: absolute; left: 395px; top: 66px; width: 265px; text-align: center; font-size: 58px; font-weight: 400; color: var(--gold); letter-spacing: 1px; }
  .brand__dot { display: inline-block; width: 14px; height: 14px; border-radius: 50%; background: var(--gold); margin-right: 10px; vertical-align: middle; }
  .tagline { position: absolute; font-family: "Marck Script", cursive; color: var(--gold); font-size: 36px; font-weight: 400; }
  .tagline--top { left: 352px; top: 192px; }
  .tagline--bottom { left: 494px; top: 250px; }

  .photo { position: absolute; border-style: solid; }
  .photo--slush { left: 14px; top: -2px; width: 264px; height: 302px; border-width: 7px; border-color: var(--frame-pink); transform: rotate(-1deg);
    background: linear-gradient(180deg, #e9ecec 0%, #c92d3c 30%, #d23844 70%, #efefef 100%); }
  .photo--juice { left: 12px; top: 268px; width: 306px; height: 452px; border-width: 8px; border-color: var(--frame-yellow); transform: rotate(1.5deg);
    background: linear-gradient(180deg, #5fb6e6 0%, #a9d9ef 35%, #f6b63a 55%, #f3a72c 80%, #c49c7a 100%); }
  .photo--coffee { left: 24px; top: 708px; width: 276px; height: 314px; border-width: 8px; border-color: var(--frame-blue); transform: rotate(-1.5deg);
    background: linear-gradient(180deg, #111 0%, #3a2a20 30%, #c99f7e 55%, #9a6b48 80%, #2a1a10 100%); }

  .menu { position: absolute; left: 341px; width: 372px; }
  .menu__head { display: flex; justify-content: space-between; align-items: baseline; font-size: 30px; line-height: 38px; border-bottom: 3px solid var(--navy); padding-bottom: 1px; }
  .menu__items { list-style: none; font-size: 25px; line-height: 38px; margin-top: 8px; }
  .menu__note { position: absolute; right: 0; font-family: "Marck Script", cursive; font-size: 15px; line-height: 17px; text-align: center; width: 130px; }

  .menu--frozen { top: 340px; }
  .menu--juices { top: 513px; }
  .menu--coffee { top: 788px; }
  .menu--juices .menu__note, .menu--coffee .menu__note { top: 46px; }
</style>
</head>
<body>
  <main class="flyer">
    <div class="flyer__header"></div>
    <div class="flyer__edge"></div>
    <div class="flyer__footer"></div>

    <div class="brand"><span class="brand__dot"></span>solavita</div>
    <div class="tagline tagline--top">New Summer</div>
    <div class="tagline tagline--bottom">Drinks Menu</div>

    <div class="photo photo--slush" role="img" aria-label="Photo of a red frozen fruit drink with a basil sprig"></div>
    <div class="photo photo--juice" role="img" aria-label="Photo of a tall glass of orange juice with an orange slice and cocktail umbrella on a beach"></div>
    <div class="photo photo--coffee" role="img" aria-label="Photo of an iced latte topped with whipped cream on coffee beans"></div>

    <section class="menu menu--frozen">
      <h2 class="menu__head"><span>FROZEN FRUITS DRINK</span><span>£2.95</span></h2>
      <ul class="menu__items">
        <li>Strawberry and banana</li>
        <li>Pineapple, mango and banana</li>
      </ul>
    </section>

    <section class="menu menu--juices">
      <h2 class="menu__head"><span>FRUIT JUICES</span><span>£2.95</span></h2>
      <p class="menu__note">Add Mint or Ginger<br>for Free!</p>
      <ul class="menu__items">
        <li>Orange and carrot</li>
        <li>Orange and pineapple</li>
        <li>Pineapple and apple</li>
        <li>Apple and kiwi</li>
        <li>Carrot and ginger</li>
      </ul>
    </section>

    <section class="menu menu--coffee">
      <h2 class="menu__head"><span>ICED COFFEES</span><span>£2.45</span></h2>
      <p class="menu__note">Add Syrup Shot<br>for 10p</p>
      <ul class="menu__items">
        <li>Iced Coffee</li>
        <li>Iced Latte</li>
        <li>Iced Chocolate Drink</li>
      </ul>
    </section>
  </main>
</body>
</html>
```